Dunwick Realty & Management, LLC
Sunny Florida Real Estate -- Business Card - Real Estate
Sunny Florida Real Estate -- Business Card
Professional
Marcus Tolver, CRS
Broker / REALTOR®
4875 Briar Creek Lane Tallahassee, FL 32398-1147
marcustolver@dunwickrealty.example
www.dunwickrealty.example
BK5804419
Incorporate head shot into front of card.
marcustolver marcustolver
Mailing address has been changed: The new address for the business card is: 2609 Hollow Ash Court Tallahassee, FL 32398-2256
Zip code is 32398-2274

```html
<!DOCTYPE html>
<html lang="en">
<head>
<meta charset="utf-8">
<title>Dunwick Realty &amp; Management — Stationery</title>
<link href="https://fonts.googleapis.com/css2?family=Open+Sans:wght@400;600;700&display=swap" rel="stylesheet">
<style>
:root{
  --bg:#3a3a3a;
  --panel:#222222;
  --card-dark:#141414;
  --lime:#b3c91a;
  --lime-light:#e2ec8c;
  --paper:#ffffff;
  --ink:#333333;
  --muted:#9a9a9a;
  --line:#d6d6d6;
}
*{box-sizing:border-box;margin:0;padding:0}
html,body{width:1200px;height:204px;overflow:hidden;background:var(--bg);font-family:"Open Sans",Arial,sans-serif;color:var(--ink)}
.suite{position:relative;width:1200px;height:204px}
.piece{position:absolute;overflow:hidden}
.brand{font-weight:700;color:var(--lime);text-transform:uppercase;letter-spacing:.04em;display:flex;align-items:center;gap:3px;line-height:1.15;white-space:nowrap}
.brand .dot{width:6px;height:6px;border-radius:50%;background:var(--lime);flex:none}
.brand.stack{flex-direction:column;gap:2px;text-align:center}
.txt{font-size:3px;line-height:1.45;color:var(--muted);white-space:nowrap}
.bars span{display:block;height:1.4px;background:var(--line);margin-top:2.2px}

/* intro panel */
.intro{left:0;top:0;width:150px;height:204px;background:var(--panel);padding:9px 8px}
.intro .brand{font-size:5.5px}
.intro .tagline{font-size:4.5px;color:var(--muted);margin-top:3px;padding-left:9px}
.biz-dark{left:8px;width:134px;height:34px;background:var(--card-dark);border-left:3px solid var(--lime);padding:4px 5px;color:#fff;display:flex;gap:5px}
.biz-dark .headshot{width:20px;height:26px;flex:none}
.biz-dark .name{font-size:5.5px;font-weight:700}
.biz-dark .role{font-size:4px;color:var(--lime)}
.biz-dark .line{font-size:3.4px;color:#cfcfcf;line-height:1.4;white-space:nowrap}

.headshot{background:linear-gradient(#a3abb3,#58606a)}

/* letterhead */
.letter{top:22px;width:84px;height:168px;background:var(--paper);padding:8px 7px;border-bottom:3px solid var(--lime)}
.letter .brand{font-size:3.6px}
.letter .brand .dot{width:10px;height:10px}
.letter .body{margin-top:16px}
.letter .sign{font-size:3px;color:var(--muted);margin-top:6px;line-height:1.5}
.letter .foot{position:absolute;bottom:5px;left:6px;right:6px;font-size:2.6px;color:var(--muted);text-align:center;white-space:nowrap}

/* photo card */
.photo-card{left:462px;top:86px;width:96px;height:36px;background:var(--paper);display:flex;gap:4px;padding:3px;border-bottom:3px solid var(--lime)}
.photo-card .headshot{width:24px;height:100%;flex:none}
.photo-card .name{font-size:4.8px;font-weight:700}
.photo-card .role{font-size:3.2px;color:var(--lime);font-weight:600}

/* envelopes */
.envelope{background:var(--paper);border-bottom:3px solid var(--lime);padding:4px 5px}
.envelope .brand{font-size:3.4px}
.envelope .brand .dot{width:5px;height:5px}
.envelope .to{position:absolute;left:42%;top:48%}
.envelope.back{background:linear-gradient(160deg,#fff 48%,#ececec 49% 51%,#fff 52%)}

.usb{height:20px;border-radius:4px;background:var(--lime);display:flex;align-items:center;justify-content:center}
.usb.light{background:var(--paper)}
.usb .dot{width:6px;height:6px;border-radius:50%;background:#fff}
.usb.light .dot{background:var(--lime)}

.folder{top:18px;height:172px}
.folder.lime{left:816px;width:94px;background:radial-gradient(circle at 50% 42%,var(--lime-light),var(--lime) 70%);display:flex;align-items:center;justify-content:center}
.folder.lime .brand{color:#fff;font-size:4.6px}
.folder.lime .brand .dot{background:#fff;width:14px;height:14px}
.folder.white{left:912px;width:74px;background:var(--paper);border-bottom:4px solid var(--lime);padding:10px 7px}
.folder.white .brand{font-size:3.2px}

.disc{left:1000px;top:18px;width:90px;height:90px;border-radius:50%;background:radial-gradient(circle,var(--bg) 0 7%,#fff 8% 12%,var(--lime-light) 13% 34%,var(--lime) 35%);display:flex;align-items:flex-end;justify-content:center;padding-bottom:16px;overflow:visible}
.disc .brand{font-size:3.6px;color:#fff}

.id-card{left:986px;top:156px;width:58px;height:30px;background:var(--paper);border-top:4px solid var(--lime);padding:3px;display:flex;gap:3px}
.id-card .headshot{width:14px;height:20px;flex:none}
.id-card .name{font-size:3.6px;font-weight:700}

.screen{background:var(--paper);border:3px solid #0e0e0e;border-radius:4px;display:flex;align-items:center;justify-content:center}
.screen .brand{font-size:3.2px}
</style>
</head>
<body>
<main class="suite">

  <section class="piece intro">
    <div class="brand"><span class="dot"></span>Dunwick Realty &amp; Management, LLC</div>
    <div class="tagline">Welcome to Dunwick</div>
  </section>
  <div class="piece biz-dark" style="top:100px">
    <div class="headshot" role="img" aria-label="Head shot of Marcus Tolver"></div>
    <div>
      <div class="name">Marcus Tolver, CRS</div>
      <div class="role">Broker / REALTOR®</div>
      <div class="line">2609 Hollow Ash Court Tallahassee, FL 32398-2256</div>
    </div>
  </div>
  <div class="piece biz-dark" style="top:142px">
    <div class="headshot" role="img" aria-label="Head shot of Marcus Tolver"></div>
    <div>
      <div class="line">marcustolver@dunwickrealty.example</div>
      <div class="line">www.dunwickrealty.example</div>
      <div class="line">License BK5804419</div>
    </div>
  </div>

  <article class="piece letter" style="left:158px">
    <div class="brand stack"><span class="dot"></span>Dunwick Realty</div>
    <div class="body">
      <div class="txt">Dear Client,</div>
      <div class="bars"><span></span><span></span><span></span><span style="width:70%"></span></div>
      <div class="bars" style="margin-top:5px"><span></span><span></span><span></span><span></span><span style="width:55%"></span></div>
      <div class="bars" style="margin-top:5px"><span></span><span></span><span style="width:80%"></span></div>
    </div>
    <div class="sign">Sincerely,<br>Marcus Tolver</div>
    <div class="foot">2609 Hollow Ash Court Tallahassee, FL 32398-2256</div>
  </article>
  <article class="piece letter" style="left:252px">
    <div class="brand stack"><span class="dot"></span>Dunwick Realty</div>
    <div class="body">
      <div class="txt">Dear Client,</div>
      <div class="bars"><span></span><span></span><span></span><span style="width:65%"></span></div>
      <div class="bars" style="margin-top:5px"><span></span><span></span><span></span><span style="width:60%"></span></div>
      <div class="bars" style="margin-top:5px"><span></span><span></span><span></span><span style="width:75%"></span></div>
    </div>
    <div class="sign">Sincerely,<br>Marcus Tolver</div>
    <div class="foot">www.dunwickrealty.example</div>
  </article>

  <div class="piece photo-card">
    <div class="headshot" role="img" aria-label="Head shot of Marcus Tolver"></div>
    <div>
      <div class="name">Marcus Tolver, CRS</div>
      <div class="role">Broker / REALTOR®</div>
      <div class="txt" style="font-size:2.7px">2609 Hollow Ash Court<br>Tallahassee, FL 32398-2274<br>marcustolver@dunwickrealty.example<br>www.dunwickrealty.example</div>
    </div>
  </div>

  <div class="piece usb" style="left:696px;top:24px;width:32px"><span class="dot"></span></div>
  <div class="piece usb light" style="left:734px;top:24px;width:32px"><span class="dot"></span></div>

  <div class="piece envelope back" style="left:612px;top:70px;width:110px;height:44px"><div class="brand"><span class="dot"></span>Dunwick Realty</div></div>
  <div class="piece envelope" style="left:612px;top:122px;width:110px;height:30px">
    <div class="brand"><span class="dot"></span>Dunwick Realty</div>
    <div class="txt to" style="font-size:2.6px">Client Name<br>Street Address, City</div>
  </div>
  <div class="piece envelope" style="left:612px;top:158px;width:110px;height:30px">
    <div class="txt" style="font-size:2.6px">2609 Hollow Ash Court<br>Tallahassee, FL 32398-2256</div>
  </div>

  <div class="piece folder lime"><div class="brand stack"><span class="dot"></span>Dunwick Realty</div></div>
  <div class="piece folder white">
    <div class="brand"><span class="dot"></span>Dunwick Realty</div>
    <div class="bars" style="margin-top:14px"><span></span><span></span><span style="width:70%"></span></div>
    <div class="txt" style="position:absolute;bottom:8px;left:7px;font-size:2.6px">www.dunwickrealty.example<br>BK5804419</div>
  </div>

  <div class="piece disc"><div class="brand">Dunwick</div></div>

  <div class="piece envelope" style="left:1098px;top:22px;width:86px;height:40px">
    <div class="brand"><span class="dot"></span>Dunwick Realty</div>
    <div class="txt to" style="left:36%;font-size:2.6px">Client Name<br>Street Address, City</div>
  </div>
  <div class="piece envelope back" style="left:1098px;top:70px;width:86px;height:44px"></div>

  <div class="piece id-card">
    <div class="headshot" role="img" aria-label="ID photo of Marcus Tolver"></div>
    <div>
      <div class="name">Marcus Tolver</div>
      <div class="txt" style="font-size:2.6px">Broker / REALTOR®</div>
    </div>
  </div>

  <div class="piece screen" style="left:1052px;top:128px;width:52px;height:62px"><div class="brand stack"><span class="dot"></span>Dunwick</div></div>
  <div class="piece screen" style="left:1118px;top:140px;width:28px;height:50px"><div class="brand stack"><span class="dot"></span></div></div>

</main>
</body>
</html>
```